High End Business Card Design for Flooring Store

Looking for a new card design for our hardwood flooring company. We have no print budget for these and are open to cards made from wood, metal, cardstock with embossed print ... or any combination of these. No plastic.

We sell luxury products and I want the cards to reflect our image of quality and class.

Our contact information as such;
Employee Name
418 Colbrook Blvd.
Lindmere, ON
K9R-3M5
(555) 214-3968
Employee email @velkaflooring.com

Target Market(s)

Home Builders

Contact Information for Business Card

Emnployee name, business contact information

```html
<!DOCTYPE html>
<html lang="en">
<head>
<meta charset="utf-8">
<title>Velka Flooring – Business Card</title>
<link rel="stylesheet" href="https://fonts.googleapis.com/css2?family=Montserrat:wght@500&family=Lato:wght@400&display=swap">
<style>
  :root {
    --backdrop: #1c1511;
    --wood-light: #5e3d2a;
    --wood-mid: #503322;
    --wood-dark: #43291c;
    --band: #2a1a15;
    --ink: #ffffff;
  }
  html, body {
    margin: 0;
    padding: 0;
    width: 1200px;
    height: 1193px;
    overflow: hidden;
    background: var(--backdrop);
  }
  .card {
    position: absolute;
    left: 239px;
    width: 721px;
    height: 411px;
    color: var(--ink);
  }
  .card--front { top: 124px; }
  .card--back { top: 619px; }
  .card__shape {
    position: absolute;
    inset: 0;
    width: 721px;
    height: 411px;
  }
  .brand-name {
    position: absolute;
    left: 0;
    width: 100%;
    margin: 0;
    text-align: center;
    font-family: "Montserrat", sans-serif;
    font-weight: 500;
    line-height: 1;
    letter-spacing: 0.01em;
  }
  .card--front .brand-name { top: 36px; font-size: 104px; }
  .card--back .brand-name { top: 96px; font-size: 116px; }
  .tagline {
    position: absolute;
    left: 0;
    width: 100%;
    margin: 0;
    text-align: center;
    font-family: "Montserrat", sans-serif;
    font-weight: 500;
  }
  .card--front .tagline { top: 134px; font-size: 24px; line-height: 28px; }
  .card--back .tagline { top: 205px; font-size: 27px; line-height: 31px; }
  .employee-name {
    position: absolute;
    left: 75px;
    top: 208px;
    margin: 0;
    font-family: "Lato", sans-serif;
    font-size: 31px;
    font-weight: 400;
  }
  .divider {
    position: absolute;
    left: 355px;
    top: 209px;
    width: 2px;
    height: 156px;
    background: var(--ink);
  }
  .contact {
    position: absolute;
    left: 376px;
    top: 217px;
    margin: 0;
    padding: 0;
    list-style: none;
    font-family: "Lato", sans-serif;
    font-size: 21px;
    line-height: 27px;
  }
  .contact__item {
    position: relative;
    padding-left: 36px;
  }
  .contact__icon {
    position: absolute;
    left: 0;
    top: 3px;
    width: 24px;
    height: 24px;
  }
  .website {
    position: absolute;
    left: 0;
    width: 100%;
    top: 337px;
    margin: 0;
    text-align: center;
    font-family: "Lato", sans-serif;
    font-size: 21px;
    letter-spacing: 0.55em;
  }
</style>
</head>
<body>
<svg width="0" height="0" style="position:absolute">
  <defs>
    <clipPath id="card-outline">
      <path d="M50 0 H671 Q700 0 708 30 Q735 205 708 381 Q700 411 671 411 H50 Q21 411 13 381 Q-14 205 13 30 Q21 0 50 0 Z"/>
    </clipPath>
    <linearGradient id="wood-tone" x1="0" y1="0" x2="0" y2="1">
      <stop offset="0" stop-color="#5e3d2a"/>
      <stop offset="0.5" stop-color="#4f3222"/>
      <stop offset="1" stop-color="#5a3926"/>
    </linearGradient>
  </defs>
</svg>

<section class="card card--front">
  <svg class="card__shape" viewBox="0 0 721 411" role="img" aria-label="Hardwood plank texture card face">
    <g clip-path="url(#card-outline)">
      <rect width="721" height="411" fill="url(#wood-tone)"/>
      <rect width="721" height="23" fill="var(--band)"/>
      <rect y="385" width="721" height="26" fill="var(--band)"/>
    </g>
  </svg>
  <h1 class="brand-name">Velka</h1>
  <p class="tagline">Planchers &amp; Escaliers<br>Flooring &amp; Stairs</p>
  <p class="employee-name">Employee Name</p>
  <div class="divider"></div>
  <ul class="contact">
    <li class="contact__item">
      <svg class="contact__icon" viewBox="0 0 24 24" fill="none" stroke="#fff" stroke-width="1.6">
        <path d="M12 22 C7 15 5 12 5 9 a7 7 0 0 1 14 0 c0 3-2 6-7 13z"/>
        <circle cx="12" cy="9" r="2.5"/>
      </svg>
      418 Colbrook Blvd.<br>Lindmere, ON<br>K9R-3M5
    </li>
    <li class="contact__item">
      <svg class="contact__icon" viewBox="0 0 24 24" fill="none" stroke="#fff" stroke-width="1.6" stroke-linejoin="round">
        <path d="M6 3 l3 0 l2 5 l-2.5 1.5 a12 12 0 0 0 6 6 l1.5-2.5 l5 2 l0 3 a2 2 0 0 1-2 2 A17 17 0 0 1 4 5 a2 2 0 0 1 2-2z"/>
      </svg>
      (555) 214-3968
    </li>
    <li class="contact__item">
      <svg class="contact__icon" viewBox="0 0 24 24" fill="none" stroke="#fff" stroke-width="1.6">
        <rect x="2" y="6" width="20" height="13"/>
        <path d="M2 6 l10 8 l10-8 M2 19 l7-7 M22 19 l-7-7"/>
      </svg>
      email @velkaflooring.com
    </li>
  </ul>
</section>

<section class="card card--back">
  <svg class="card__shape" viewBox="0 0 721 411" role="img" aria-label="Hardwood plank texture card face">
    <g clip-path="url(#card-outline)">
      <rect width="721" height="411" fill="url(#wood-tone)"/>
      <rect width="721" height="23" fill="var(--band)"/>
      <rect y="385" width="721" height="26" fill="var(--band)"/>
    </g>
  </svg>
  <h2 class="brand-name">Velka</h2>
  <p class="tagline">Planchers &amp; Escaliers<br>Flooring &amp; Stairs</p>
  <p class="website">velkaflooring.com</p>
</section>
</body>
</html>
```